Vitalune - Label design for a supplement with probiotic and prebiotic

Hello, we are a supplement company and we need a label design for our first product. The product's name is Vitalune and the company's name is Koravex Nutrition (Logo attached, It is allowed to change the color) and we are located in Orlando, if we like the label, in the future we can make other products too.
Our product is a supplement that contains probiotics, prebiotics and other vitamins, it will be packaged in a 300g plastic jar (Img attached), we like simple but premium-looking packaging.
Below are some links to brands and products we like:
https://www.shopvarelt.example/stores/page/7D1188AA-5521-4E9B-B302-B1A447FE22CC?ingress=2&visitId=91b2ccd4-774e-408a-bb21-c4e8f1aa2093&ref_=bl_dp_s_web_58213044022
https://www.shopvarelt.example/stores/page/61AB4E3D-92C1-4A77-9D20-7EE350173B81?ingress=2&visitId=8812fa0e-311c-4d2a-a7f4-1b9c30e44f12&ref_=bl_dp_s_web_24417720933
https://www.shopvarelt.example/stores/Teluvo+Nutrition/page/C2288340-5E61-4B19-93A4-12307C88D29E?store_ref=SLP_FW_450D77AB-C12E-4A98-A31F-2207E5C9A611
https://www.shopvarelt.example/stores/page/AA2C46DE-71F9-4B22-C390-5EEDC81B309F?ingress=2&visitId=15e93b27-6a0c-4f3e-9bd1-a7c2301ee9b4&ref_=bl_dp_s_web_4182930055
https://www.shopvarelt.example/stores/node/39527164022?_encoding=UTF8&field-lbr_brands_browse-bin=QUILMAXNUTRITION&ref_=bl_dp_s_web_39527164022
https://www.shopvarelt.example/stores/page/2B3E8804-6611-4C2A-9F17-E8A913B02C57?ingress=6&visitId=4461d09c-b12a-4d7e-8fa1-09c5d3e6bb21&store_ref=storeRecs_Instant_27316488033
Updates
Hi, This product will be packaged in a 300g bottle, it is allowed to insert images and it is very important to inform "100 Billion live bacteria", 5 grams of probiotic, 5 grams of prebiotic and orange flavor.
The bottle is rounded, the size of the art must be 2.87 in and 10.74 in, I will need barcode space, supplement facts, directions and warning. This information I can put later.
Target Market(s)
Our target is people who wish to have a healthier recovery after undergoing cancer treatments, helping to maintain health, improving quality of life and reducing the harm that these treatments cause.
Requirements
Must have
- It is very important that the product contains the following information:
- 100 Billion live bacteria
- 5 grams of probiotic and 5 grams of prebiotic
- No artificial flavours
- Space for barcode
Amount per container: 10.6 oz (300 g)
Serving size: 1 scoop (10 grams)
Servings per container: 30
Amount per serving
Calories 15 Calories from fat 0
Total Fat 0
Total Carbohydrate 5g
Dietary fiber 4g
Sugars 1g
Protein 0g
Proprietary Probiotic blend: 5 billons
Lactobacillus acidophilus
Bifidobacterium animalis subsp. lactis.
Other ingredients: Organic inulin fiber, stevia, natural orange flavor, citric acid, riboflavin Not a significant source of cholesterol, fat and protein
Nice to have
- We like simple design
Should not have
- Images from brolen photos.

```html
<!DOCTYPE html>
<html lang="en">
<head>
<meta charset="utf-8">
<title>Koravex Nutrition – Probiotic &amp; Prebiotic Label</title>
<link rel="stylesheet" href="https://fonts.googleapis.com/css2?family=Roboto+Slab:wght@500;700;800&family=Tinos:wght@400;700&family=Roboto+Condensed:wght@400&family=Libre+Franklin:wght@400;600;800;900&display=swap">
<style>
  :root {
    --green: #2db57a;
    --grey: #a6a6a6;
    --rule: #b9b9b9;
    --ink: #1e1e1e;
    --paper: #ffffff;
    --backdrop: #ececec;
    --barcode: #c4c4c5;
  }
  * { margin: 0; padding: 0; box-sizing: border-box; }
  html, body { width: 1200px; height: 926px; overflow: hidden; background: var(--backdrop); }

  .label {
    position: absolute; left: 40px; top: 296px;
    width: 1120px; height: 334px;
    background: var(--paper);
    box-shadow: 0 6px 14px rgba(0,0,0,.18);
    font-family: "Tinos", serif;
    color: var(--ink);
  }
  .band { position: absolute; left: 0; right: 0; height: 13px; background: var(--green); }
  .band--top { top: 0; }
  .band--bottom { bottom: 0; }

  /* left panel */
  .info { position: absolute; left: 19px; top: 40px; width: 345px; }
  .info h3 {
    font-family: "Roboto Slab", serif; font-weight: 500;
    color: var(--green); font-size: 13px; margin-bottom: 3px;
  }
  .info p { font-size: 9.6px; line-height: 11.8px; margin-bottom: 14px; }
  .warning {
    position: absolute; left: 19px; top: 200px; width: 333px; height: 50px;
    border: 2px solid #333; padding: 6px 10px;
    font-size: 9.6px; line-height: 11.5px;
  }
  .warning strong { font-weight: 400; font-size: 12.5px; display: block; line-height: 13px; }
  .warning span { font-weight: 700; }

  .badge { position: absolute; top: 264px; width: 80px; margin-left: -40px; text-align: center; }
  .badge__mark {
    display: block; width: 36px; height: 36px; margin: 0 auto 5px;
    border-radius: 50%; border: 2px solid var(--green);
  }
  .badge__mark--solid { background: var(--green); }
  .badge__name {
    font-family: "Roboto Condensed", sans-serif; font-size: 10.5px;
    color: var(--green); white-space: nowrap;
  }

  /* centre panel */
  .front { position: absolute; left: 429px; top: 38px; width: 261px; }
  .brand {
    font-family: "Roboto Slab", serif; font-weight: 700;
    color: var(--green); font-size: 19.5px; letter-spacing: .2px;
    text-align: center; white-space: nowrap;
  }
  .title {
    position: relative; margin-top: 7px; height: 86px;
    border-top: 2px solid var(--rule); border-bottom: 2px solid var(--rule);
  }
  .title__word {
    position: absolute; left: 0;
    font-family: "Roboto Slab", serif; font-weight: 800;
    color: var(--grey); font-size: 31px; letter-spacing: .5px; line-height: 1;
    white-space: nowrap;
  }
  .title__word--one { top: 8px; }
  .title__word--two { top: 45px; }
  .title__amp {
    position: absolute; right: 2px; top: -4px;
    font-family: "Roboto Slab", serif; font-weight: 800;
    color: var(--grey); font-size: 82px; line-height: 1;
  }
  .count {
    font-family: "Roboto Slab", serif; font-weight: 500;
    font-size: 22.5px; text-align: center; margin-top: 5px; white-space: nowrap;
  }
  .claims { display: flex; align-items: center; margin-top: 6px; height: 34px; }
  .claim {
    display: flex; align-items: center; gap: 4px; color: var(--green);
    font-family: "Roboto Slab", serif; padding: 0 6px;
    border-left: 2px solid var(--green);
  }
  .claim:first-child { border-left: 0; padding-left: 0; }
  .claim:last-child { padding-right: 0; }
  .claim__big { font-size: 26px; font-weight: 700; line-height: 1; }
  .claim__small { font-size: 12px; line-height: 11.5px; }
  .cta {
    margin-top: 18px; height: 35px;
    background: var(--green); color: #fff;
    border-radius: 22px 22px 6px 6px / 18px 18px 6px 6px;
    font-family: "Tinos", serif; font-weight: 700; font-size: 14px;
    display: flex; align-items: center; justify-content: center; letter-spacing: .2px;
  }
  .weight {
    margin-top: 11px; text-align: center;
    font-weight: 700; font-size: 10px; color: var(--green); letter-spacing: .2px;
  }

  .decor {
    position: absolute; left: 700px; top: 62px; width: 124px; height: 196px;
    background: radial-gradient(ellipse at center, #ebebeb 0%, #f6f6f6 55%, #ffffff 80%);
    border-radius: 40px;
  }

  /* facts panel */
  .facts {
    position: absolute; left: 862px; top: 20px; width: 224px;
    border: 2px solid #111; padding: 2px 3px 3px;
    font-family: "Libre Franklin", sans-serif; font-size: 9px; line-height: 12px;
    white-space: nowrap;
  }
  .facts h2 { font-weight: 900; font-size: 24px; line-height: 26px; letter-spacing: .2px; }
  .facts .row { display: flex; justify-content: space-between; border-top: 1px solid #333; }
  .facts .row--indent { padding-left: 10px; }
  .facts .row b { font-weight: 800; }
  .facts .pct { font-weight: 800; }
  .facts .thick { border-top: 6px solid #111; }
  .facts .mid { border-top: 3px solid #111; }
  .facts .small { font-size: 7.6px; line-height: 10px; font-weight: 600; }
  .facts .vit { font-size: 8.6px; line-height: 11px; }
  .facts i { font-style: italic; }
  .facts .plain { border-top: 0; }

  .maker { position: absolute; left: 862px; top: 282px; color: var(--grey); }
  .maker h4 { font-family: "Tinos", serif; font-weight: 400; font-size: 13px; line-height: 14px; }
  .maker p { font-size: 9.4px; line-height: 11.5px; }
  .barcode-space {
    position: absolute; left: 970px; top: 278px; width: 124px; height: 42px;
    background: var(--barcode);
  }
</style>
</head>
<body>
<main class="label">
  <div class="band band--top"></div>

  <section class="info">
    <h3>Directions</h3>
    <p>Lorem ipsum dolor sit amet, consectetuer adipiscing elit, sed diam nonummy nibh euismod tincidunt ut laoreet dolore magna aliquam erat volutpat. Ut wisi enim ad minim veniam, quis nostrud exerci tation ullamcorper suscipit lobortis nisl ut aliquip ex ea commodo consequat. Duis autem vel eum iriure dolor in hendrerit in vulputate velit esse molestie consequat.</p>
    <h3>How to Use</h3>
    <p>Lorem ipsum dolor sit amet, consectetuer adipiscing elit, sed diam nonummy nibh euismod tincidunt ut laoreet dolore magna aliquam erat</p>
  </section>
  <div class="warning">
    <strong>WARNING</strong>
    <span>Lorem ipsum dolor sit amet, consectetuer adipiscing elit, sed diam nonummy nibh euismod tincidunt ut laoreet dolore erat.</span>
  </div>

  <div class="badge" style="left:84px"><span class="badge__mark"></span><span class="badge__name">Gluten Free</span></div>
  <div class="badge" style="left:150px"><span class="badge__mark"></span><span class="badge__name">Lactose Free</span></div>
  <div class="badge" style="left:227px"><span class="badge__mark"></span><span class="badge__name">Kosher Certified</span></div>
  <div class="badge" style="left:295px"><span class="badge__mark badge__mark--solid"></span><span class="badge__name">Non GMO</span></div>

  <section class="front">
    <div class="brand">KORAVEX NUTRITION</div>
    <div class="title">
      <span class="title__word title__word--one">PROBIOTIC</span>
      <span class="title__word title__word--two">PREBIOTIC</span>
      <span class="title__amp">&amp;</span>
    </div>
    <div class="count">100 Billion live bacteria</div>
    <div class="claims">
      <div class="claim"><span class="claim__big">5</span><span class="claim__small">grams of<br>probiotic</span></div>
      <div class="claim"><span class="claim__big">5</span><span class="claim__small">grams of<br>prebiotic</span></div>
      <div class="claim"><span class="claim__big">No</span><span class="claim__small">artificial<br>flavours</span></div>
    </div>
    <div class="cta">DIETARY SUPPLEMENT</div>
    <div class="weight">NET WT. 485G (1.07 LBS)</div>
  </section>

  <div class="decor" role="img" aria-label="Faint grey molecule network illustration"></div>

  <section class="facts">
    <h2>Nutrition Facts</h2>
    <div class="row plain"><span>Serving Size 95 g</span></div>
    <div class="row thick small"><b>Amount Per Serving</b></div>
    <div class="row"><span><b>Calories</b> 231</span><span>Calories from Fat 154</span></div>
    <div class="row mid small" style="justify-content:flex-end"><span>% Daily Value*</span></div>
    <div class="row"><span><b>Total Fat</b> 17.2g</span><span class="pct">26%</span></div>
    <div class="row row--indent"><span>Saturated Fat 5.8g</span><span class="pct">29%</span></div>
    <div class="row row--indent"><span><i>Trans</i> Fat 0.0g</span><span></span></div>
    <div class="row"><span><b>Cholesterol</b> 0mg</span><span class="pct">0%</span></div>
    <div class="row"><span><b>Sodium</b> 87mg</span><span class="pct">4%</span></div>
    <div class="row"><span><b>Potassium</b> 293mg</span><span class="pct">8%</span></div>
    <div class="row"><span><b>Total Carbohydrates</b> 18.6g</span><span class="pct">6%</span></div>
    <div class="row row--indent"><span>Dietary Fiber 5.3g</span><span class="pct">21%</span></div>
    <div class="row row--indent"><span>Sugars 11.0g</span><span></span></div>
    <div class="row"><span><b>Protein</b> 2.5g</span><span></span></div>
    <div class="row thick vit"><span>Vitamin A 2%</span><span>•</span><span>Vitamin C 10%</span></div>
    <div class="row plain vit"><span>Calcium 4%</span><span>•</span><span>Iron 2%</span></div>
  </section>

  <div class="maker">
    <h4>Manufacture:</h4>
    <p>Koravex Nutrition<br>Ph: 0100 555 0142</p>
  </div>
  <div class="barcode-space"></div>

  <div class="band band--bottom"></div>
</main>
</body>
</html>
```